Letterhead for New Orthopaedic Surgery Practice

My husband and I are starting our own practice named RB Spine & Vitality Center. We would like to create a nice simple but high class letterhead that doesn't use too much solid color ink when printing. I like the colors dark blue, gold, yellow. Open to other suggestions. We will need to list him and I both on the top of the letterhead. Here is the important information:
Lucinda Perrow, M.D. - Hand and Upper Extremity Surgery
Abena Quist, M.D. - Hip & Knee Replacement/General Orthopaedic Surgery
Location: 18735 North Harlow Pkwy
Palm Hollow, FL 33520
Phone: 954-218-4650
Fax: 954-582-1346
Email: info@myrbspine.com

The only thing is that the phone and fax numbers will change once we get into our space. I just want to get the design started. I am including several documents which are my previous practice letterhead, my current procedure room letterhead, and our new Logo. The other letterheads are just for examples but please think outside of the box! We would love to see some great designs.

Colors
0054AA
0677BA
7BADD7
CADEEF
E8F1F8
0094D4
00A9DD
6FCCEA
C7EBF8
E9F6FB

Requirements
Must have
• class, elegance, luxury

```html
<!DOCTYPE html>
<html lang="en">
<head>
<meta charset="utf-8">
<title>RB Spine &amp; Vitality Center — Letterhead</title>
<link rel="stylesheet" href="https://fonts.googleapis.com/css2?family=Tinos:wght@400;700&display=swap">
<style>
  :root {
    --navy: #17173f;
    --gold: #b8954f;
    --paper: #f5f6f9;
    --backdrop: #e3e6ef;
    --ink: #2a2a35;
    --rule: #3a3a48;
    --watermark: #c9ccd6;
    --watermark-ring: #e3dccb;
  }
  * { box-sizing: border-box; margin: 0; padding: 0; }
  html, body { width: 1200px; height: 800px; overflow: hidden; }
  body {
    background: var(--backdrop);
    font-family: "Tinos", "Times New Roman", serif;
    color: var(--ink);
    position: relative;
  }
  .letterhead {
    position: absolute;
    left: 300px; top: 12px;
    width: 600px; height: 776px;
    background: var(--paper);
    box-shadow: 0 6px 22px rgba(30, 30, 70, 0.18);
    overflow: hidden;
  }
  .letterhead__header {
    position: absolute;
    left: 30px; right: 30px; top: 34px;
    height: 86px;
    display: flex;
    align-items: center;
    border-bottom: 1px solid var(--rule);
  }
  .brand {
    display: flex;
    align-items: center;
    gap: 7px;
    color: var(--navy);
    font-weight: 700;
    font-size: 12px;
    line-height: 1.15;
    width: 118px;
    flex: none;
  }
  .brand__dot {
    width: 12px; height: 12px;
    border-radius: 50%;
    background: var(--gold);
    flex: none;
  }
  .physicians {
    margin-left: auto;
    text-align: right;
    font-size: 9.5px;
    line-height: 1.35;
    padding-right: 10px;
    white-space: nowrap;
  }
  .physicians__name { font-weight: 700; color: var(--navy); }
  .divider {
    width: 1px; height: 58px;
    background: var(--rule);
    flex: none;
  }
  .contact {
    list-style: none;
    padding-left: 10px;
    font-size: 9.5px;
    line-height: 1.35;
    white-space: nowrap;
    flex: none;
  }
  .contact li { display: flex; align-items: flex-start; gap: 6px; }
  .contact svg { width: 9px; height: 9px; margin-top: 2px; flex: none; fill: var(--gold); }
  .watermark {
    position: absolute;
    left: 50%; top: 300px;
    transform: translateX(-50%);
    width: 300px; height: 300px;
    border: 2px solid var(--watermark-ring);
    border-radius: 50%;
    display: flex;
    align-items: center;
    justify-content: center;
    text-align: center;
    color: var(--watermark);
    font-size: 34px;
    font-weight: 700;
    line-height: 1.15;
    padding: 30px;
  }
  .letterhead__footer {
    position: absolute;
    left: 0; bottom: 0;
    width: 600px; height: 240px;
  }
</style>
</head>
<body>
  <main class="letterhead">
    <header class="letterhead__header">
      <div class="brand">
        <span class="brand__dot"></span>
        <span class="brand__name">RB Spine &amp; Vitality Center</span>
      </div>
      <div class="physicians">
        <p class="physicians__name">Lucinda Perrow, M.D.</p>
        <p class="physicians__specialty">Hand and Upper Extremity Surgery</p>
        <p class="physicians__name">Abena Quist, M.D.</p>
        <p class="physicians__specialty">Hip &amp; Knee Replacement/General Orthopaedic Surgery</p>
      </div>
      <span class="divider"></span>
      <ul class="contact">
        <li><svg viewBox="0 0 10 10" aria-hidden="true"><path d="M2 0.5 L4 2.8 L3 4 Q4.3 6 6 7 L7.2 6 L9.5 8 L8.2 9.5 Q3.5 9 0.5 1.8 Z"/></svg>954-218-4650</li>
        <li><svg viewBox="0 0 10 10" aria-hidden="true"><rect x="0.5" y="3" width="9" height="6.5" rx="0.8"/><rect x="2.5" y="0.5" width="5" height="3"/></svg>954-582-1346</li>
        <li><svg viewBox="0 0 10 10" aria-hidden="true"><path d="M0.5 2 H9.5 V8.5 H0.5 Z M0.5 2 L5 5.8 L9.5 2"/></svg>info@myrbspine.com</li>
        <li><svg viewBox="0 0 10 10" aria-hidden="true"><path d="M5 0.3 A3.5 3.5 0 0 1 8.5 3.8 C8.5 6 5 9.7 5 9.7 C5 9.7 1.5 6 1.5 3.8 A3.5 3.5 0 0 1 5 0.3 Z M5 2.6 A1.2 1.2 0 1 0 5 5 A1.2 1.2 0 1 0 5 2.6 Z"/></svg><span>18735 North Harlow Pkwy<br>Palm Hollow, FL 33520</span></li>
      </ul>
    </header>

    <div class="watermark" aria-hidden="true">RB Spine &amp; Vitality Center</div>

    <svg class="letterhead__footer" viewBox="0 0 600 240" preserveAspectRatio="none" aria-hidden="true">
      <path d="M0 224 C180 202 330 152 440 72 C500 32 560 16 600 10 V240 H0 Z" fill="var(--gold)"/>
      <path d="M0 228 C190 206 340 158 450 80 C508 40 565 22 600 16 V240 H0 Z" fill="var(--paper)"/>
      <path d="M0 232 C200 212 350 165 460 88 C515 50 568 32 600 26 V240 H0 Z" fill="var(--navy)"/>
    </svg>
  </main>
</body>
</html>
```